Kestrel Signs Facebook Banner Design

Design a facebook banner for a sign company. I would like to have a modern approach to it.

Product Offering:
Signs
Banners
Decals
Commercial Wraps

```html
<!DOCTYPE html>
<html lang="en">
<head>
<meta charset="utf-8">
<title>Kestrel Signs – Facebook Banner</title>
<link rel="stylesheet" href="https://fonts.googleapis.com/css2?family=Russo+One&family=Exo+2:ital,wght@1,500&display=swap">
<style>
  :root {
    --page: #fefefe;
    --navy: #10065f;
    --plum: #4a0230;
    --crimson: #a2000f;
    --red: #e80000;
    --cyan: #7ee8ff;
    --magenta: #ff3fbf;
    --sky: #5aa8ff;
    --white: #ffffff;
  }
  html, body {
    margin: 0;
    width: 1200px;
    height: 848px;
    overflow: hidden;
    background: var(--page);
  }
  .canvas {
    position: relative;
    width: 1200px;
    height: 848px;
  }
  .banner {
    position: absolute;
    left: 170px;
    top: 242px;
    width: 838px;
    height: 311px;
    display: block;
  }
  .service-label {
    font-family: "Exo 2", sans-serif;
    font-style: italic;
    font-weight: 500;
    fill: var(--white);
  }
  .service-frame {
    fill: none;
    stroke: var(--white);
    stroke-width: 1.2;
  }
  .brand-name {
    font-family: "Russo One", sans-serif;
    fill: var(--white);
  }
  .dash-line {
    stroke: var(--sky);
    stroke-width: 1.4;
    stroke-dasharray: 8 10;
  }
</style>
</head>
<body>
<div class="canvas">
  <svg class="banner" viewBox="0 0 838 311" xmlns="http://www.w3.org/2000/svg">
    <defs>
      <linearGradient id="bg-sweep" x1="0" y1="0" x2="1" y2="0">
        <stop offset="0" stop-color="var(--navy)"/>
        <stop offset="0.45" stop-color="var(--plum)"/>
        <stop offset="0.75" stop-color="var(--crimson)"/>
        <stop offset="1" stop-color="var(--red)"/>
      </linearGradient>
      <radialGradient id="light-burst" cx="0.02" cy="0.5" r="0.9" gradientTransform="scale(1 0.55) translate(0 0.4)">
        <stop offset="0" stop-color="var(--cyan)" stop-opacity="0.95"/>
        <stop offset="0.18" stop-color="var(--magenta)" stop-opacity="0.7"/>
        <stop offset="0.55" stop-color="#7a4fd0" stop-opacity="0.35"/>
        <stop offset="1" stop-color="#7a4fd0" stop-opacity="0"/>
      </radialGradient>
    </defs>

    <rect class="banner-bg" width="838" height="311" fill="url(#bg-sweep)"/>

    <rect class="speed-streaks" role="img" aria-label="Abstract speed-of-light streaks in cyan, magenta and violet rushing from the left edge"
          x="0" y="40" width="620" height="230" fill="url(#light-burst)"/>

    <g class="dash-lines">
      <line class="dash-line" x1="275" y1="176" x2="410" y2="178"/>
      <line class="dash-line" x1="264" y1="266" x2="320" y2="272"/>
      <line class="dash-line" x1="345" y1="280" x2="400" y2="287"/>
      <line class="dash-line" x1="118" y1="82" x2="175" y2="78"/>
    </g>

    <g class="service service--signs">
      <polygon class="service-frame" points="333,104 358,80 489,75 461,101"/>
      <text class="service-label" x="411" y="96" font-size="17" text-anchor="middle" transform="rotate(-3 411 90)">Signs</text>
    </g>

    <g class="service service--banners">
      <polygon class="service-frame" points="209,170 235,152 359,150 335,172"/>
      <text class="service-label" x="283" y="168" font-size="15" text-anchor="middle" transform="rotate(2 283 162)">Banners</text>
    </g>

    <g class="service service--decals">
      <polygon class="service-frame" points="202,253 228,231 346,244 321,269"/>
      <text class="service-label" x="272" y="255" font-size="17" text-anchor="middle" transform="rotate(7 272 249)">Decals</text>
    </g>

    <g class="service service--wraps">
      <polygon class="service-frame" points="3,254 21,236 222,270 197,290"/>
      <text class="service-label" x="111" y="267" font-size="15" text-anchor="middle" transform="rotate(10 111 262)">Commercial Wraps</text>
    </g>

    <g class="brand">
      <text class="brand-name" x="631" y="162" font-size="56" text-anchor="middle" textLength="358" lengthAdjust="spacingAndGlyphs">KESTREL</text>
      <text class="brand-name" x="636" y="206" font-size="46" text-anchor="middle" textLength="180" lengthAdjust="spacingAndGlyphs">SIGNS</text>
    </g>
  </svg>
</div>
</body>
</html>
```